KR business cards
Business cards for Consulting outfit
Project: KR business cards
KR business cards -
Creative Brief
Professional
No name
No address
info@vosk-lantern.example
vosk-lantern.example
Would like business cards for 8 different people. No address on the card
Logo + We define the standard

```html
<!DOCTYPE html>
<html lang="en">
<head>
<meta charset="utf-8">
<title>vosk-lantern stationery</title>
<link rel="stylesheet" href="https://fonts.googleapis.com/css2?family=PT+Serif:wght@400;700&display=swap">
<style>
  :root {
    --backdrop: #8c8c8c;
    --paper: #ffffff;
    --ink: #3a3a3a;
    --ink-soft: #777777;
    --accent: #b5343b;
    --fold: #d6d6d6;
  }
  * { margin: 0; padding: 0; box-sizing: border-box; }
  html, body { width: 1200px; height: 626px; overflow: hidden; }
  body {
    background: var(--backdrop);
    font-family: "PT Serif", Georgia, serif;
    color: var(--ink);
    position: relative;
  }
  .sheet { position: absolute; background: var(--paper); }

  .brand { display: flex; align-items: center; gap: 6px; color: var(--ink); font-weight: 400; }
  .brand-square { background: var(--accent); flex: none; }

  /* business cards */
  .card-back { left: 34px; top: 240px; width: 139px; height: 82px; }
  .card-back .person { position: absolute; left: 10px; top: 9px; font-size: 6px; line-height: 1.35; }
  .card-back .person strong { display: block; font-size: 6.5px; }
  .card-back .brand { position: absolute; left: 10px; top: 38px; font-size: 10px; }
  .card-back .brand-square { width: 7px; height: 7px; }
  .card-back .contact { position: absolute; left: 10px; bottom: 7px; font-size: 4.5px; line-height: 1.4; color: var(--ink-soft); }

  .card-front { left: 34px; top: 338px; width: 139px; height: 82px; }
  .card-front .brand { position: absolute; left: 10px; top: 34px; font-size: 10px; }
  .card-front .brand-square { width: 9px; height: 9px; }
  .card-front .web { position: absolute; right: 8px; bottom: 6px; font-size: 4.5px; color: var(--accent); }

  /* letterhead */
  .letterhead { left: 199px; top: 19px; width: 509px; height: 600px; }
  .letterhead .brand { position: absolute; left: 40px; top: 28px; font-size: 12px; }
  .letterhead .brand-square { width: 10px; height: 10px; }
  .recipient { position: absolute; left: 40px; top: 78px; font-size: 8px; font-weight: 700; line-height: 1.4; }
  .letter-body { position: absolute; left: 40px; top: 130px; width: 430px; font-size: 9.5px; line-height: 1.7; }
  .letter-body p { margin-bottom: 12px; text-align: justify; }
  .signature { position: absolute; left: 40px; top: 450px; width: 110px; height: 36px; background: linear-gradient(90deg, #2a2a2a22, #2a2a2a55, #2a2a2a22); border-radius: 18px; }
  .letter-contact { position: absolute; left: 40px; top: 522px; font-size: 6px; line-height: 1.5; color: var(--ink-soft); }
  .letter-block { position: absolute; right: 0; bottom: 8px; width: 32px; height: 32px; background: var(--accent); }

  /* envelope */
  .envelope { left: 758px; top: 180px; width: 413px; height: 434px; }
  .envelope .flap { position: absolute; left: 0; top: 0; }
  .envelope .brand { position: absolute; left: 150px; top: 376px; top: 372px; font-size: 12px; }
  .envelope .brand-square { width: 10px; height: 10px; }
  .envelope .brand { top: 196px; }
  .envelope-contact { position: absolute; left: 40px; bottom: 30px; font-size: 6px; line-height: 1.5; color: var(--ink-soft); }
  .envelope-block { position: absolute; right: 14px; bottom: 40px; width: 46px; height: 46px; background: var(--accent); }
</style>
</head>
<body>

  <section class="sheet card-back" aria-label="Business card, contact side">
    <div class="person"><strong>Ada Marsh</strong>Senior Consultant</div>
    <div class="brand"><span class="brand-square"></span>vosk-lantern</div>
    <div class="contact">+1 555 0142<br>info@vosk-lantern.example</div>
  </section>

  <section class="sheet card-front" aria-label="Business card, brand side">
    <div class="brand"><span class="brand-square"></span>vosk-lantern</div>
    <div class="web">vosk-lantern.example</div>
  </section>

  <section class="sheet letterhead" aria-label="Letterhead">
    <div class="brand"><span class="brand-square"></span>vosk-lantern</div>
    <div class="recipient">Lorem Ipsum<br>dolor sit amet<br>consectetur adipiscing elit</div>
    <div class="letter-body">
      <p>Dear client, thank you for the time you gave our team last week. We have reviewed your goals and prepared a short outline of the steps we propose for the coming quarter.</p>
      <p>Our first phase maps current processes, interviews key staff and sets clear measures of success. The second phase tests small changes in one unit before they are rolled out across the wider business. Each phase ends with a written review.</p>
      <p>Fees follow the schedule attached to this letter and are billed monthly. Travel and materials are charged at cost, with no added margin. Either side may pause the work with thirty days of written notice.</p>
      <p>Please let us know if the plan suits you. We would be glad to meet again and answer any questions.</p>
      <p>Sincerely yours,</p>
    </div>
    <div class="signature" role="img" aria-label="Handwritten signature"></div>
    <div class="letter-contact">+1 555 0100<br>info@vosk-lantern.example<br>vosk-lantern.example</div>
    <div class="letter-block"></div>
  </section>

  <section class="sheet envelope" aria-label="Envelope">
    <svg class="flap" width="413" height="60" viewBox="0 0 413 60" aria-hidden="true">
      <polyline points="0,0 206,55 413,0" fill="none" stroke="var(--fold)" stroke-width="1.5"/>
    </svg>
    <div class="brand"><span class="brand-square"></span>vosk-lantern</div>
    <div class="envelope-contact">+1 555 0100<br>info@vosk-lantern.example<br>vosk-lantern.example</div>
    <div class="envelope-block"></div>
  </section>

</body>
</html>
```